ZEPHIRO needs a new business card!

ZEPHIRO is a group of gaming enthusiasts who are looking for a new corporate business card.

The typeface should be modern and minimalist with attention paid to spacing between the letters and the letters 'zephiro' look relative to each other.

Should clean, crisp and minimalist - looking serious overall but with slight tweaks to the letters to make them look playful...

Black on white is fine.

Details on the card should include:
-the word 'zephiro'
-a job title (use any, for e.g. founder)
-a name (e.g. Ned Falka)
-phone number
-email address

For inspiration: http://brisket.tumblevane-cdn.example/wp-content/uploads/2013/07/mela-1.jpg

Target Market(s)

Video gaming enthusiasts

Industry/Entity Type

Business

Requirements
Must have
• Black letter on white background.
The word "zephiro"
Nice to have
• Maybe use a conservative font like Gibraltar or Helvetica and tweaking each letter individually.

You can insert normal job titles under the "zephiro" typeface
Should not have
• Should not be cartoony or childish fonts. No colors.

```html
<!DOCTYPE html>
<html lang="en">
<head>
<meta charset="UTF-8">
<title>ZEPHIRO Business Card</title>
<link rel="stylesheet" href="https://fonts.googleapis.com/css2?family=Marcellus+SC&family=Open+Sans:wght@400&display=swap">
<style>
  :root {
    --ink: #000000;
    --paper: #ffffff;
    --paper-edge: #f7f8f8;
    --muted: #8c8c8c;
    --frame: #111111;
  }
  * { margin: 0; padding: 0; box-sizing: border-box; }
  html, body {
    width: 1200px;
    height: 1000px;
    overflow: hidden;
    background: var(--paper);
  }
  .card {
    position: absolute;
    left: 62px;
    top: 32px;
    width: 1065px;
    height: 616px;
    border: 1px solid var(--frame);
    border-radius: 2px;
    background: radial-gradient(ellipse 60% 70% at 50% 50%, var(--paper) 55%, var(--paper-edge) 100%);
    font-family: "Marcellus SC", serif;
    color: var(--ink);
  }
  .brand-name {
    position: absolute;
    left: 0;
    right: 0;
    top: 190px;
    text-align: center;
    font-size: 128px;
    line-height: 1;
    letter-spacing: 0.02em;
    color: var(--ink);
  }
  .tagline {
    position: absolute;
    left: 10px;
    right: 0;
    top: 372px;
    text-align: center;
    font-family: "Open Sans", sans-serif;
    font-size: 25px;
    letter-spacing: 0.62em;
    color: var(--muted);
  }
  .contact-line {
    position: absolute;
    left: 0;
    right: 0;
    top: 494px;
    display: flex;
    justify-content: center;
    align-items: baseline;
    white-space: nowrap;
    font-size: 24px;
    letter-spacing: 0.03em;
  }
  .person-name {
    font-size: 31px;
    letter-spacing: 0.06em;
    -webkit-text-stroke: 0.6px var(--ink);
    margin-right: 10px;
  }
  .job-title { margin-right: 20px; }
  .icon {
    align-self: center;
    fill: var(--ink);
  }
  .icon-phone { width: 22px; height: 28px; margin-right: 8px; }
  .phone { margin-right: 18px; }
  .icon-mail { width: 30px; height: 22px; margin-right: 16px; }
</style>
</head>
<body>
  <main class="card">
    <div class="brand-name">ZEPHIRO</div>
    <p class="tagline">GAMING ENTHUSIASTS</p>
    <div class="contact-line">
      <span class="person-name">NED FALKA</span>
      <span class="job-title">MANAGER</span>
      <svg class="icon icon-phone" viewBox="0 0 22 28" aria-hidden="true">
        <path d="M4 1 L9 1 L10 8 L7 10 C8 14 10 18 13 21 L16 19 L21 23 L19 27 C15 28 10 25 6 18 C2 11 1 6 4 1 Z"/>
      </svg>
      <span class="phone">011-402-58-217390</span>
      <svg class="icon icon-mail" viewBox="0 0 30 22" aria-hidden="true">
        <path d="M0 0 H30 V3 L15 13 L0 3 Z"/>
        <path d="M0 6 L15 16 L30 6 V22 H0 Z"/>
      </svg>
      <span class="email">HELLO@ZEPHIRO.EXAMPLE</span>
    </div>
  </main>
</body>
</html>
```